BrightForge /

We need a logo and letterhead for a startup Dental Laboratory in New Zealand. The business makes things like dentures, crowns, implants and night guards on prescription from dentists. The appliances are fabricated then shipped back to the dentist who recalls the patient and fits them. We are looking for a minimilist, very professional design. We don't want any play on words or mention of smiles or anything to do with apples. Would like the name to read
"BrightForge" and then a tag line " Innovative Laboratory Solutions"
Not that fussed on a logo other than maybe BF. The final design should communicate contemporary professionalism, innovation and an eye for detail.

```html
<!DOCTYPE html>
<html lang="en">
<head>
<meta charset="utf-8">
<title>BrightForge Letterhead</title>
<link href="https://fonts.googleapis.com/css2?family=Questrial&display=swap" rel="stylesheet">
<style>
  :root {
    --navy: #2f5777;
    --teal: #5aa7c4;
    --ink: #3a3d42;
    --paper: #f6f6f5;
    --backdrop: #d8d8da;
    --rule: #b9bcc0;
    --sig-tint: #dfe3f2;
  }
  * { box-sizing: border-box; margin: 0; padding: 0; }
  html, body { width: 1200px; height: 1152px; overflow: hidden; }
  body {
    background: var(--backdrop);
    font-family: "Questrial", "Century Gothic", sans-serif;
    color: var(--ink);
  }
  .letterhead {
    position: absolute;
    left: 210px; top: 26px;
    width: 780px; height: 1100px;
    background: var(--paper);
    overflow: hidden;
  }
  .header-band { position: absolute; left: 0; top: 0; width: 780px; height: 70px; }
  .brand { position: absolute; left: 65px; top: 66px; }
  .brand-name {
    font-size: 38px; line-height: 38px;
    color: var(--navy); letter-spacing: 0.5px;
  }
  .brand-tagline {
    margin-top: 4px;
    font-size: 10px; letter-spacing: 1.1px;
    text-transform: uppercase; color: var(--ink);
  }
  .letter-text { font-size: 11.5px; line-height: 14px; }
  .date { position: absolute; left: 65px; top: 279px; }
  .recipient { position: absolute; left: 65px; top: 307px; }
  .salutation { position: absolute; left: 65px; top: 426px; font-weight: bold; }
  .body-copy {
    position: absolute; left: 65px; top: 454px; width: 651px;
    text-align: justify;
  }
  .body-copy p + p { margin-top: 14px; }
  .closing { position: absolute; left: 65px; top: 762px; }
  .closing .signer { font-weight: bold; }
  .signature-area {
    position: absolute; left: 162px; top: 738px;
    width: 165px; height: 85px;
    background: var(--sig-tint);
  }
  .contact-bar {
    position: absolute; left: 65px; top: 985px;
    width: 651px; height: 78px;
    display: flex;
  }
  .contact-item {
    flex: 1;
    display: flex; flex-direction: column; align-items: center;
    padding-top: 8px;
    font-size: 11.5px; line-height: 14px; text-align: center;
  }
  .contact-item + .contact-item { border-left: 1px solid var(--rule); }
  .contact-item svg { width: 24px; height: 26px; margin-bottom: 14px; }
  .contact-item .icon-line { fill: none; stroke: var(--teal); stroke-width: 1.8; }
  .contact-item .icon-fill { fill: var(--teal); }
</style>
</head>
<body>
  <main class="letterhead">
    <svg class="header-band" viewBox="0 0 780 70" aria-hidden="true">
      <path d="M0,14 C250,10 560,32 780,62 L780,66 C560,38 250,22 0,24 Z" fill="var(--teal)"/>
      <path d="M0,0 H780 V60 C560,29 250,6 0,11 Z" fill="var(--navy)"/>
    </svg>

    <div class="brand">
      <div class="brand-name">BrightForge</div>
      <div class="brand-tagline">Innovative Laboratory Solutions</div>
    </div>

    <div class="letter-text date">30.09.2016</div>
    <div class="letter-text recipient">
      Recipient’s name<br>Lindenweg 14<br>10115 Berlin<br>Germany
    </div>

    <div class="letter-text salutation">Dear sir,</div>

    <div class="letter-text body-copy">
      <p>Communication is a very integral part of living creatures, animals and humans. Communication may be verbal or written. Written communication however is only applicable to human beings. Can you even imagine a world without communication? Verbal communication can be through telephones, webcams or in person. Written communication is through letters, emails and mobile phone messages.</p>
      <p>In today’s world of great inventions and technology, letters have somehow become redundant. It is the time for text messages or chats. But they still can communicate a lot more than all other modes of communication. Organizations and various government departments still bank on letters as a strong medium of communication. There is no comparison in costs of sending letters as compared to costs of mobile phone messages though – letters are far cheaper. Letters now commonly known as “hard copy documents” are considered more relevant and important than email copies of text messages as proof or evidence of some sort.</p>
      <p>Letters speak volumes about a person or an organization that writes it. So one must take utmost care ensuring that the language used in any letter is appropriate for the occasion for which it is being written. Since a letter is also a written proof or document, if there are certain things that should not form a part of it, then that too should be carefully handled.</p>
      <p>Writing a good letter is an art. But if for some reason someone is unable to write that perfect letter, these different types of letters provide a base for you to build on. Sample letters have been given for everyone to understand what all information needs to form a part of the letter type and then it can be customized.</p>
    </div>

    <div class="letter-text closing">
      Yours Sincerely,<br><span class="signer">Corin Vale</span>
    </div>
    <div class="signature-area" role="img" aria-label="Handwritten signature of Corin Vale in blue ink"></div>

    <footer class="contact-bar">
      <div class="contact-item">
        <svg viewBox="0 0 24 26" aria-hidden="true">
          <path class="icon-line" d="M12,24 C6,16 4,12 4,9 A8,8 0 0 1 20,9 C20,12 18,16 12,24 Z"/>
          <circle class="icon-line" cx="12" cy="9" r="3"/>
        </svg>
        <span>218 Harbour Lane<br>Nelson 7010</span>
      </div>
      <div class="contact-item">
        <svg viewBox="0 0 24 26" aria-hidden="true">
          <path class="icon-fill" d="M6,3 L10,3 L11,9 L8.5,10.5 C10,14 12,16.5 15.5,18 L17,15.5 L22,17 L22,21 C22,22 21,23 19.5,23 C11,22 4,15 3,6 C3,4.5 4.5,3 6,3 Z"/>
        </svg>
        <span>021.448.3196</span>
      </div>
      <div class="contact-item">
        <svg viewBox="0 0 24 26" aria-hidden="true">
          <rect class="icon-line" x="7" y="3" width="10" height="7"/>
          <rect class="icon-fill" x="2" y="10" width="20" height="10" rx="1.5"/>
          <rect x="6" y="16" width="12" height="6" fill="var(--paper)" stroke="var(--teal)" stroke-width="1.5"/>
        </svg>
        <span>021.448.3207</span>
      </div>
      <div class="contact-item">
        <svg viewBox="0 0 24 26" aria-hidden="true">
          <circle class="icon-line" cx="12" cy="13" r="10"/>
          <ellipse class="icon-line" cx="12" cy="13" rx="4.5" ry="10"/>
          <path class="icon-line" d="M2,13 H22 M4,8 H20 M4,18 H20"/>
        </svg>
        <span>www.brightforge.co.nz</span>
      </div>
    </footer>
  </main>
</body>
</html>
```